LMR Nursing Care

I am a registered nurse with a private nursing care service.
We provide the following care;
Registered Nursing, Palliative Nursing, personal care, dementia repite, day respite , overnight respite, domestic assistance, welfare checks, and transport.
In the community, our service is brochured by service providers and we also supply to private clients.

Target Market(s)

Aged care, disabled clients, dementia clients in the community

Industry/Entity Type

Nurse

Font styles to use
Sans Serif

Colors
6b449b
e44699
b868aa

Requirements
Must have
• Contact: Rosalind Pemberly - Registered Nurse
PO Box 587 Marrowby
0437 261 508
Nice to have
• A soft caring picture feature

```html
<!DOCTYPE html>
<html lang="en">
<head>
<meta charset="utf-8">
<title>LMR Nursing Care – Card</title>
<link href="https://fonts.googleapis.com/css2?family=Montserrat:wght@700;800&family=Mulish:wght@500;600;700&display=swap" rel="stylesheet">
<style>
  :root {
    --pink: #e44699;
    --purple: #6b449b;
    --mauve: #b868aa;
    --white: #ffffff;
    --ink: #1a1a1a;
    --blush: #fbe6f1;
    --backdrop: #d9dadc;
  }
  * { box-sizing: border-box; margin: 0; padding: 0; }
  html, body { width: 927px; height: 1200px; overflow: hidden; }
  body {
    background: var(--backdrop);
    font-family: "Mulish", sans-serif;
    position: relative;
  }
  .card {
    position: absolute;
    left: 138px;
    width: 650px;
    height: 470px;
    background: var(--pink);
    box-shadow: 0 6px 18px rgba(0,0,0,0.25);
  }
  .card--front { top: 70px; }
  .card--back { top: 660px; }

  .panel {
    position: absolute;
    left: 25px; top: 25px;
    width: 600px; height: 420px;
    border-radius: 14px;
    background: radial-gradient(ellipse at 40% 45%, var(--white) 40%, var(--blush) 100%);
    overflow: hidden;
  }
  .panel__frame {
    position: absolute;
    left: 8px; top: 50px; right: 8px; bottom: 8px;
    border: 1px solid var(--pink);
    border-radius: 10px;
  }
  .edge-dot {
    position: absolute;
    z-index: 2;
    width: 22px; height: 22px;
    border-radius: 50%;
    border: 3px solid var(--pink);
    background: var(--white);
  }
  .edge-dot--left { left: 14px; top: 285px; }
  .edge-dot--right { right: 14px; top: 205px; }

  .title-band {
    position: absolute;
    left: 18px; top: 18px;
    width: 530px; height: 50px;
    background: var(--purple);
    border-radius: 8px;
    color: var(--white);
    font-family: "Montserrat", sans-serif;
    font-weight: 800;
    font-size: 25px;
    line-height: 50px;
    text-align: center;
    white-space: nowrap;
  }
  .intro {
    position: absolute;
    left: 40px; top: 80px;
    font-size: 16.5px;
    font-weight: 600;
    color: var(--ink);
    white-space: nowrap;
  }
  .care-heading {
    position: absolute;
    left: 80px; top: 110px;
    font-family: "Montserrat", sans-serif;
    font-weight: 700;
    font-size: 13px;
    color: var(--ink);
  }
  .care-list {
    position: absolute;
    left: 86px; top: 132px;
    list-style: none;
  }
  .care-list li {
    font-size: 15px;
    font-weight: 600;
    color: var(--ink);
    line-height: 24px;
    white-space: nowrap;
  }
  .care-list li::before {
    content: "";
    display: inline-block;
    width: 7px; height: 7px;
    background: var(--ink);
    transform: rotate(45deg);
    margin-right: 8px;
    vertical-align: 2px;
  }
  .care-list li:nth-child(2) { padding-left: 3px; }
  .care-list li:nth-child(3) { padding-left: 6px; }
  .care-list li:nth-child(4) { padding-left: 9px; }
  .care-list li:nth-child(5) { padding-left: 12px; }
  .care-list li:nth-child(6) { padding-left: 15px; }
  .care-list li:nth-child(7) { padding-left: 18px; }
  .care-list li:nth-child(8) { padding-left: 21px; }

  .photo {
    position: absolute;
    left: 385px; top: 108px;
    width: 145px; height: 205px;
    border-radius: 70px 70px 0 0;
    background: linear-gradient(180deg, #e9d9cf 0%, #8fb0d8 45%, #7a9ccc 100%);
  }
  .wave {
    position: absolute;
    left: 0; top: 0;
    width: 600px; height: 420px;
  }
  .contact-divider {
    position: absolute;
    left: 418px; top: 296px;
    width: 2px; height: 96px;
    background: var(--white);
  }
  .contact {
    position: absolute;
    left: 422px; top: 304px;
    width: 172px;
    text-align: center;
    color: var(--white);
  }
  .contact__name {
    font-family: "Montserrat", sans-serif;
    font-weight: 700;
    font-size: 13px;
    white-space: nowrap;
  }
  .contact__role { font-size: 14px; font-weight: 600; margin-bottom: 12px; }
  .contact__line { font-size: 14px; font-weight: 700; line-height: 17px; white-space: nowrap; }
  .footer-note {
    position: absolute;
    left: 22px; top: 384px;
    width: 385px;
    color: var(--white);
    font-weight: 700;
    font-size: 12.5px;
    line-height: 15px;
  }

  .back-label {
    position: absolute;
    right: 50px; bottom: 70px;
    width: 240px; height: 180px;
    background: #f1f1f1;
    border-radius: 26px;
    text-align: center;
    color: var(--pink);
    padding-top: 28px;
  }
  .back-label__name {
    font-family: "Montserrat", sans-serif;
    font-weight: 700;
    font-size: 18px;
    white-space: nowrap;
  }
  .back-label__role { font-size: 19px; font-weight: 600; }
  .back-label__rule {
    position: relative;
    width: 150px; height: 2px;
    background: var(--pink);
    margin: 8px auto 14px;
  }
  .back-label__rule::before, .back-label__rule::after {
    content: "";
    position: absolute;
    top: -3px;
    width: 8px; height: 8px;
    border-radius: 50%;
    background: var(--pink);
  }
  .back-label__rule::before { left: -4px; }
  .back-label__rule::after { right: -4px; }
  .back-label__line { font-size: 18px; font-weight: 700; line-height: 23px; white-space: nowrap; }
</style>
</head>
<body>

  <section class="card card--front">
    <div class="panel">
      <div class="panel__frame"></div>
      <div class="title-band">PRIVATE NURSING CARE SERVICE</div>
      <p class="intro">I am a registered nurse with a private nursing care service.</p>
      <p class="care-heading">WE PROVIDE THE FOLLOWING CARE</p>
      <ul class="care-list">
        <li>Registered Nursing</li>
        <li>Palliative Nursing</li>
        <li>personal care</li>
        <li>dementia repite</li>
        <li>day respite</li>
        <li>overnight respite</li>
        <li>domestic assistance</li>
        <li>welfare checks, and transport.</li>
      </ul>
      <div class="photo" role="img" aria-label="Photo of a smiling nurse in blue scrubs with a stethoscope, holding a clipboard"></div>
      <svg class="wave" viewBox="0 0 600 420" aria-hidden="true">
        <path d="M0 328 C130 420 290 360 410 290 C480 250 545 240 600 246 L600 420 L0 420 Z" fill="#b868aa"/>
        <path d="M0 328 C130 420 290 360 410 290 C480 250 545 240 600 246" fill="none" stroke="#6b449b" stroke-width="5"/>
      </svg>
      <div class="contact-divider"></div>
      <div class="contact">
        <p class="contact__name">ROSALIND PEMBERLY</p>
        <p class="contact__role">Registered Nurse</p>
        <p class="contact__line">PO Box 587 Marrowby</p>
        <p class="contact__line">0437 261 508</p>
      </div>
      <p class="footer-note">In the community, our service is brochured by service providers and we also supply to private clients.</p>
    </div>
    <div class="edge-dot edge-dot--left"></div>
    <div class="edge-dot edge-dot--right"></div>
  </section>

  <section class="card card--back">
    <div class="back-label">
      <p class="back-label__name">ROSALIND PEMBERLY</p>
      <p class="back-label__role">Registered Nurse</p>
      <div class="back-label__rule"></div>
      <p class="back-label__line">PO Box 587 Marrowby</p>
      <p class="back-label__line">0437 261 508</p>
    </div>
  </section>

</body>
</html>
```